Clean Stationary Design For Print Shop

I need a clean stationary set that properly represents a local print and copy shop to make it look amazing. It should do the following:
- Compliment the color scheme of the logo.
- Be clean and sharp.
- Be colorful but but balanced.

This is what I need designed:
- Business Card
- Letter Head
- Envelop

Target Market(s)

Local customers and businesses, including hospitals and schools.

Industry/Entity Type

Digital Printing

Requirements
Must have
• Clean business card with logo on front and full color back with faded logo on it and social icons with @hollowmeadowsco beside each one (Facebook & Instagram).

```html
<!DOCTYPE html>
<html lang="en">
<head>
<meta charset="utf-8">
<title>Hollow Meadows – Business Card</title>
<link rel="stylesheet" href="https://fonts.googleapis.com/css2?family=Montserrat:wght@800&family=Open+Sans:wght@400;600;700&family=Arimo:wght@400&display=swap">
<style>
  :root {
    --backdrop: #e6e6e4;
    --paper: #f7f7f7;
    --ink: #111111;
    --black: #000000;
    --red: #f0304f;
    --red-deep: #b81c34;
    --grey: #6b6b6b;
    --rule: #8a8a8a;
    --white: #ffffff;
  }
  * { box-sizing: border-box; margin: 0; padding: 0; }
  html, body { width: 1200px; height: 801px; overflow: hidden; }
  body {
    background: var(--backdrop);
    position: relative;
    font-family: "Arimo", Arial, sans-serif;
  }
  .card {
    position: absolute;
    top: 252px;
    width: 520px;
    height: 297px;
    overflow: hidden;
    box-shadow: 0 6px 18px rgba(0,0,0,.18);
  }
  .card--front { left: 60px; background: linear-gradient(135deg, #eeeeee, var(--paper) 60%, #ececec); }
  .card--back { left: 620px; background: var(--black); }

  .card__swoosh { position: absolute; inset: 0; }

  .brand {
    position: absolute;
    left: 30px;
    top: 130px;
    display: flex;
    align-items: center;
    gap: 9px;
  }
  .brand__mark { width: 20px; height: 20px; background: var(--red); flex: none; }
  .brand__name {
    font-family: "Open Sans", sans-serif;
    font-weight: 600;
    font-size: 19px;
    color: var(--ink);
    line-height: 1;
    white-space: nowrap;
  }
  .brand__tagline {
    font-family: "Open Sans", sans-serif;
    font-weight: 700;
    font-size: 6.5px;
    letter-spacing: .4px;
    color: var(--grey);
    margin-top: 3px;
    white-space: nowrap;
  }

  .divider {
    position: absolute;
    left: 248px;
    top: 62px;
    width: 1px;
    height: 150px;
    background: var(--rule);
  }

  .contact { position: absolute; left: 268px; top: 56px; }
  .contact__name {
    font-family: "Montserrat", sans-serif;
    font-weight: 800;
    font-size: 22px;
    color: var(--red);
    line-height: 1.1;
  }
  .contact__role { font-size: 13px; color: var(--grey); margin-bottom: 14px; }
  .contact__list { list-style: none; }
  .contact__item {
    display: flex;
    align-items: center;
    gap: 8px;
    font-size: 12.5px;
    color: var(--grey);
    height: 21px;
    white-space: nowrap;
  }
  .contact__item svg { width: 13px; height: 13px; flex: none; fill: var(--red); }
  .contact__accent { color: var(--red); }
  .contact__social-mark { width: 12px; height: 12px; background: var(--red); flex: none; margin-right: 1px; }

  .back__panel { position: absolute; inset: 0; }
  .back__brand {
    position: absolute;
    left: 188px;
    top: 170px;
    color: var(--white);
  }
  .back__name {
    font-family: "Open Sans", sans-serif;
    font-weight: 600;
    font-size: 34px;
    line-height: 1;
    color: #f2f2f2;
    white-space: nowrap;
  }
  .back__tagline {
    font-family: "Open Sans", sans-serif;
    font-weight: 700;
    font-size: 11px;
    letter-spacing: .6px;
    color: #e4e4e4;
    margin-top: 6px;
    white-space: nowrap;
  }
</style>
</head>
<body>

  <section class="card card--front" aria-label="Business card front">
    <svg class="card__swoosh" viewBox="0 0 520 297" preserveAspectRatio="none" aria-hidden="true">
      <path d="M240 297 Q430 235 520 70 L520 297 Z" fill="var(--black)"/>
      <path d="M200 297 Q390 228 470 150 Q410 238 232 297 Z" fill="var(--red)"/>
    </svg>

    <div class="brand">
      <span class="brand__mark"></span>
      <div>
        <div class="brand__name">Hollow Meadows</div>
        <div class="brand__tagline">CRISP PRINTS, QUICK TURNAROUND</div>
      </div>
    </div>

    <div class="divider"></div>

    <div class="contact">
      <div class="contact__name">Mara Ellison</div>
      <div class="contact__role">Manager</div>
      <ul class="contact__list">
        <li class="contact__item">
          <svg viewBox="0 0 24 24"><path d="M6.6 10.8a15 15 0 0 0 6.6 6.6l2.2-2.2a1 1 0 0 1 1-.25 11.4 11.4 0 0 0 3.6.57 1 1 0 0 1 1 1V20a1 1 0 0 1-1 1A17 17 0 0 1 3 4a1 1 0 0 1 1-1h3.5a1 1 0 0 1 1 1c0 1.25.2 2.45.57 3.6a1 1 0 0 1-.25 1z"/></svg>
          555-014-2100
        </li>
        <li class="contact__item">
          <svg viewBox="0 0 24 24"><path d="M2 5h20v14H2z" fill="var(--red)"/><path d="M3 6l9 7 9-7" fill="none" stroke="var(--white)" stroke-width="1.6"/></svg>
          hello@hollowmeadows.co
        </li>
        <li class="contact__item">
          <svg viewBox="0 0 24 24"><circle cx="12" cy="12" r="10"/><path d="M2 12h20M12 2c3 3 3 17 0 20M12 2c-3 3-3 17 0 20" fill="none" stroke="var(--white)" stroke-width="1.4"/></svg>
          <span>www.<span class="contact__accent">hollowmeadows</span>.co</span>
        </li>
        <li class="contact__item">
          <span class="contact__social-mark"></span>
          @hollowmeadowsco
        </li>
      </ul>
    </div>
  </section>

  <section class="card card--back" aria-label="Business card back">
    <svg class="back__panel" viewBox="0 0 520 297" preserveAspectRatio="none" aria-hidden="true">
      <defs>
        <linearGradient id="back-red" x1="0" y1="1" x2="1" y2="0">
          <stop offset="0" stop-color="var(--red-deep)"/>
          <stop offset=".6" stop-color="var(--red)"/>
          <stop offset="1" stop-color="#5a0f1b"/>
        </linearGradient>
      </defs>
      <rect x="0" y="0" width="170" height="297" fill="url(#back-red)"/>
    </svg>
    <div class="back__brand">
      <div class="back__name">Hollow Meadows</div>
      <div class="back__tagline">CRISP PRINTS, QUICK TURNAROUND</div>
    </div>
  </section>

</body>
</html>
```